Brightmeadow Charity Ball Poster

We are looking for a poster for our upcoming event, "Brightmeadow Charity Ball" - a sit down dinner formal event hosted by our university club, OKRU.
Usually we source designs internally from our committee (even if they aren't the most amazing quality), however this time round we have no one available to do it as everyone is a volunteer.
The event's theme is 'winter wonderland', based around the snowy forests you see in Velmoria or Crown of Ashes (neither of these specific things are the theme however). Our venue is a clear-roof marque in a space surrounded by very tall pine trees giving off the forest vibe, and there are festoons strung between the trees so this is an element of warm light amongst the forest, perhaps a building or village tucked away in the forest.
The poster is for printing out at A3 size, and we will also need to create a Chatterbook event cover photo and other marketing graphics from the original poster files so some flexibility in the design and original files are required.
Things that need to be included on the poster :
---Event details
Brightmeadow Charity Ball
Saturday 12th August
7pm – midnight
Harrowgate Auditorium, KPT
Tables of 10
Members - $140
Non members - $150
All profits donated to Stride for Hope
---- Extra info and images (can be at the bottom, in corners etc,)
18+ ID required | Drink Responsibly
OKRU Logo
KPT Guild Logo
(these logos may be changed to black and white if need be)
Example images of styles, colours and the sort of landscape we want for the poster can be found in the document attached.

```html
<!DOCTYPE html>
<html lang="en">
<head>
<meta charset="utf-8">
<title>Brightmeadow Charity Ball</title>
<link href="https://fonts.googleapis.com/css2?family=Chewy&family=Philosopher:wght@400;700&display=swap" rel="stylesheet">
<style>
  :root {
    --violet: #6a3fd6;
    --indigo: #3a2a9e;
    --ice: #cfd8f5;
    --frost: #eef0fb;
    --deep: #1f2370;
    --gold-top: #fff27a;
    --gold-bottom: #f7a21a;
    --ink: #ffffff;
    --guild-blue: #1f3fd0;
    --okru-red: #a51c2e;
  }
  html, body {
    margin: 0;
    padding: 0;
    overflow: hidden;
    background: #ffffff;
  }
  .poster {
    position: relative;
    width: 849px;
    height: 1200px;
    overflow: hidden;
    font-family: "Philosopher", sans-serif;
    color: var(--ink);
  }
  .forest-backdrop {
    position: absolute;
    inset: 0;
    background:
      radial-gradient(ellipse at 85% 15%, rgba(238,240,251,0.85) 0%, rgba(238,240,251,0) 40%),
      radial-gradient(ellipse at 10% 30%, rgba(207,216,245,0.55) 0%, rgba(207,216,245,0) 35%),
      radial-gradient(ellipse at 50% 100%, rgba(238,240,251,0.9) 0%, rgba(238,240,251,0) 35%),
      linear-gradient(180deg, #7d6ae0 0%, var(--violet) 30%, var(--indigo) 55%, #4b5fd0 78%, #b9c2ef 100%);
  }
  .title {
    position: absolute;
    left: 0;
    top: 150px;
    width: 849px;
    height: 220px;
  }
  .title text {
    font-family: "Chewy", cursive;
    fill: url(#goldFill);
    filter: drop-shadow(2px 4px 4px rgba(30,20,90,0.55));
  }
  .details {
    position: absolute;
    left: 0;
    width: 849px;
    text-align: center;
    text-shadow: 0 2px 6px rgba(20,15,80,0.6);
  }
  .details p { margin: 0; }
  .event-date { top: 442px; font-size: 40px; line-height: 48px; letter-spacing: 0.5px; }
  .event-venue { font-size: 36px; line-height: 48px; }
  .pricing { top: 604px; font-size: 38px; line-height: 42px; }
  .pricing-heading {
    display: inline-block;
    border-bottom: 2px solid var(--ink);
    line-height: 40px;
  }
  .charity { top: 760px; font-size: 36px; line-height: 37px; text-transform: uppercase; }
  .fine-print { top: 866px; font-size: 29px; line-height: 37px; }
  .partner {
    position: absolute;
    display: flex;
    align-items: center;
    gap: 10px;
    font-family: "Philosopher", sans-serif;
    font-weight: 700;
    font-size: 30px;
    color: var(--ink);
  }
  .partner-mark { flex: none; }
  .partner-guild { left: 196px; top: 1080px; }
  .partner-guild .partner-mark {
    width: 28px; height: 28px; background: var(--guild-blue);
  }
  .partner-okru { left: 520px; top: 1076px; color: var(--ink); }
  .partner-okru .partner-mark {
    width: 30px; height: 30px; border-radius: 50%; background: var(--okru-red);
  }
</style>
</head>
<body>
<main class="poster">
  <div class="forest-backdrop" role="img" aria-label="Snow-covered winter forest with tall frosted trees in violet and blue light"></div>

  <svg class="title" viewBox="0 0 849 220" aria-labelledby="eventTitle">
    <title id="eventTitle">Brightmeadow Charity Ball</title>
    <defs>
      <linearGradient id="goldFill" x1="0" y1="0" x2="0" y2="1">
        <stop offset="0" stop-color="#fff27a"/>
        <stop offset="1" stop-color="#f7a21a"/>
      </linearGradient>
      <path id="arcTop" d="M 92 110 Q 424 40 760 110"/>
      <path id="arcBottom" d="M 186 170 Q 420 150 652 196"/>
    </defs>
    <text font-size="84">
      <textPath href="#arcTop" startOffset="50%" text-anchor="middle" textLength="660" lengthAdjust="spacingAndGlyphs">BRIGHTMEADOW</textPath>
    </text>
    <text font-size="78">
      <textPath href="#arcBottom" startOffset="50%" text-anchor="middle" textLength="462" lengthAdjust="spacingAndGlyphs">CHARITY BALL</textPath>
    </text>
  </svg>

  <section class="details event-date">
    <p>Saturday, 12th August</p>
    <p>7pm – midnight</p>
    <p class="event-venue">Harrowgate Auditorium, KPT</p>
  </section>

  <section class="details pricing">
    <p><span class="pricing-heading">Tables of 10</span></p>
    <p>Members - $140</p>
    <p>Non members - $150</p>
  </section>

  <section class="details charity">
    <p>All profits donated to</p>
    <p>Stride for Hope</p>
  </section>

  <section class="details fine-print">
    <p>18+ ID required</p>
    <p>Drink Responsibly</p>
  </section>

  <div class="partner partner-guild"><span class="partner-mark"></span>KPT Guild</div>
  <div class="partner partner-okru"><span class="partner-mark"></span>OKRU</div>
</main>
</body>
</html>
```